Redesign Event Flyer for Speaker

We are re-designing our professional event flyer template with new headshot and cleaner, up-to-date design. All design details are in PDF file attached. Thank you for participating :)

Font styles to use
Sans Serif

Colors
3276b5
0355a3

Requirements
Must have
• All elements in PDF file.
Nice to have
Should not have
• Tacky or childish elements.

```html
<!DOCTYPE html>
<html lang="en">
<head>
<meta charset="utf-8">
<title>The Greatest Sale – Speaker Event Flyer</title>
<link rel="stylesheet" href="https://fonts.googleapis.com/css2?family=Oswald:wght@600&family=Montserrat:wght@500;600;700&display=swap">
<style>
  :root {
    --blue-primary: #0355a3;
    --blue-accent: #3276b5;
    --blue-soft: #c4dbf1;
    --paper: #f5f8fc;
    --ink: #1b2a3d;
    --ink-muted: #4a5a6e;
    --white: #ffffff;
    --photo-top: #7a7d86;
    --photo-bottom: #1f3558;
  }
  * { margin: 0; padding: 0; box-sizing: border-box; }
  html, body {
    width: 1200px; height: 849px; overflow: hidden;
    background: var(--paper);
  }
  .flyer {
    position: relative; width: 1200px; height: 849px; overflow: hidden;
    background: var(--paper);
    font-family: "Montserrat", sans-serif;
  }
  .speaker-photo {
    position: absolute; left: 0; top: 0; width: 540px; height: 849px;
    background: linear-gradient(180deg, var(--photo-top) 0%, #6b7280 35%, var(--photo-bottom) 62%, var(--photo-bottom) 100%);
  }
  .accent-stripe {
    position: absolute; left: 540px; top: 0; width: 14px; height: 849px;
    background: var(--blue-accent);
  }
  .content {
    position: absolute; left: 620px; top: 0; width: 520px; height: 849px;
  }
  .brand {
    position: absolute; top: 60px; left: 0;
    display: flex; align-items: center; gap: 12px;
    font-weight: 700; font-size: 26px; color: var(--blue-primary);
    line-height: 1;
  }
  .brand__mark { width: 20px; height: 20px; background: var(--blue-primary); }
  .headline {
    position: absolute; top: 122px; left: 0;
    font-family: "Oswald", sans-serif; font-weight: 600;
    text-transform: uppercase; line-height: 1;
  }
  .headline__small { display: block; font-size: 52px; color: var(--blue-accent); letter-spacing: 2px; }
  .headline__large { display: block; font-size: 88px; color: var(--blue-primary); margin-top: 6px; white-space: nowrap; }
  .headline-rule {
    position: absolute; top: 304px; left: 0; width: 90px; height: 6px;
    background: var(--blue-accent);
  }
  .speaker-name {
    position: absolute; top: 336px; left: 0;
    font-weight: 600; font-size: 30px; color: var(--ink); white-space: nowrap;
  }
  .details-card {
    position: absolute; top: 430px; left: 0; width: 520px;
    padding: 34px 36px; background: var(--blue-primary); color: var(--white);
  }
  .event-date__day {
    font-weight: 600; font-size: 16px; letter-spacing: 4px;
    text-transform: uppercase; color: var(--blue-soft);
  }
  .event-date__full { font-weight: 700; font-size: 34px; margin-top: 6px; line-height: 1.1; }
  .details-card__divider {
    height: 2px; background: var(--blue-accent); margin: 26px 0;
  }
  .venue { display: flex; gap: 16px; align-items: flex-start; }
  .venue__icon { flex: 0 0 22px; margin-top: 2px; }
  .venue__name { font-weight: 700; font-size: 19px; }
  .venue__sponsor {
    display: flex; align-items: center; gap: 8px; margin: 6px 0 8px;
    font-weight: 600; font-size: 15px; color: var(--blue-soft);
  }
  .venue__sponsor-dot { width: 10px; height: 10px; border-radius: 50%; background: var(--blue-soft); }
  .venue__address { font-weight: 500; font-size: 15px; line-height: 1.5; }
  .web-links {
    position: absolute; top: 772px; left: 0;
    font-weight: 600; font-size: 16px; color: var(--blue-primary); white-space: nowrap;
  }
</style>
</head>
<body>
<main class="flyer">
  <div class="speaker-photo" role="img" aria-label="Headshot of the speaker smiling, wearing a navy blazer and white open-collar shirt"></div>
  <div class="accent-stripe"></div>

  <section class="content">
    <div class="brand"><span class="brand__mark"></span>Brightmark</div>

    <h1 class="headline">
      <span class="headline__small">The</span>
      <span class="headline__large">Greatest Sale</span>
    </h1>
    <div class="headline-rule"></div>

    <p class="speaker-name">Julian Everett Marlowe</p>

    <div class="details-card">
      <div class="event-date">
        <p class="event-date__day">Friday</p>
        <p class="event-date__full">August 9th, 2019</p>
      </div>
      <div class="details-card__divider"></div>
      <div class="venue">
        <svg class="venue__icon" width="22" height="30" viewBox="0 0 22 30">
          <path d="M11 1C5.5 1 1 5.4 1 10.9 1 18 11 29 11 29s10-11 10-18.1C21 5.4 16.5 1 11 1z" fill="var(--blue-soft)"/>
          <circle cx="11" cy="11" r="4" fill="var(--blue-primary)"/>
        </svg>
        <div>
          <p class="venue__name">Cedar Ridge Golf Club</p>
          <p class="venue__sponsor"><span class="venue__sponsor-dot"></span>Fairway</p>
          <p class="venue__address">4200 Lakeshore Pkwy<br>Riverton, Canada</p>
        </div>
      </div>
    </div>

    <p class="web-links">julianeverettmarlowe.com | brightmark.ca</p>
  </section>
</main>
</body>
</html>
```